Quorvex Labworks Website

All the descriptions are available in the attached file. The designer has to structure the website and find the right images and icons. The website should look modern and avoid using images of real humans rather use animated images. Please note that the design should include home page, all the 4 services page , the contact us would be at the bottom of home page.

```html
<!DOCTYPE html>
<html lang="en">
<head>
<meta charset="utf-8">
<title>Quorvex Labworks</title>
<link href="https://fonts.googleapis.com/css2?family=Poppins:wght@400;500;600&family=Syncopate:wght@700&display=swap" rel="stylesheet">
<style>
:root{
  --blue:#2f6db5;
  --blue-dark:#1f5aa0;
  --green:#5cb83f;
  --orange:#f7941d;
  --ink:#2b2b2b;
  --text:#3b3b3b;
  --muted:#666;
  --grey-band:#e6e4e4;
  --grey-light:#efeeee;
  --white:#fff;
}
*{margin:0;padding:0;box-sizing:border-box}
html,body{width:1200px;height:3591px;overflow:hidden}
body{position:relative;font-family:'Poppins',sans-serif;color:var(--text);background:var(--white)}
.abs{position:absolute}
.brand{display:flex;align-items:center;gap:10px;font-family:'Poppins',sans-serif;font-weight:600;color:var(--blue);font-size:23px;line-height:1.05}
.brand-mark{width:16px;height:16px;background:var(--blue);flex:none}
/* header */
.site-header{left:0;top:0;width:1200px;height:102px;background:var(--white)}
.site-header .brand{position:absolute;left:84px;top:26px}
.main-nav a{position:absolute;top:48px;font-size:15px;color:#333;text-decoration:none}
.caret{color:var(--blue);font-size:10px;margin-left:4px}
/* hero */
.hero{left:0;top:102px;width:1200px;height:520px;background:linear-gradient(100deg,#6f5b4a 0%,#9a8a78 35%,#b9b4a8 60%,#4b5a5a 100%)}
.hero::after{content:"";position:absolute;inset:0;background:rgba(20,25,30,.35)}
.hero-content{position:absolute;inset:0;z-index:1;text-align:center;color:var(--white)}
.hero h1{position:absolute;left:0;width:1200px;top:104px;font-weight:500;font-size:51px;line-height:62px}
.hero p{position:absolute;left:0;width:1200px;top:230px;font-size:15.5px;line-height:25px}
.btn{display:inline-block;background:var(--blue);color:var(--white);text-decoration:none;text-align:center;font-weight:500}
.hero .btn{position:absolute;left:503px;top:331px;width:194px;height:49px;line-height:49px;font-size:19px;border:1px solid #9fc0e6}
.dots{position:absolute;left:570px;top:399px;display:flex;gap:6px}
.dots i{width:10px;height:9px;background:rgba(255,255,255,.45)}
.dots i:first-child{background:var(--white)}
/* about */
.section-title{position:absolute;left:0;width:1200px;text-align:center}
.about-title{top:710px;font-size:44px;font-weight:600;color:var(--ink)}
.about-sub{top:766px;font-size:18px;color:#444}
.about-photo{left:85px;top:852px;width:530px;height:248px;background:linear-gradient(110deg,#6b4a3a,#b6a89a 45%,#e4e0da 65%,#7d6d60)}
.about-text{left:722px;top:859px;width:360px;font-size:15.5px;line-height:25.7px;color:#333}
.about-btn{left:722px;top:1038px;width:170px;height:50px;line-height:50px;font-size:19px}
/* services */
.services{left:0;top:1192px;width:1200px;height:717px;background:var(--grey-band)}
.wide-title{font-family:'Syncopate',sans-serif;font-weight:700;font-size:40px;color:var(--ink);letter-spacing:1px}
.service-card{position:absolute;top:1480px;width:244px;height:262px;background:var(--white);text-align:center}
.service-card h3{position:absolute;left:10px;right:10px;top:82px;font-size:18.5px;font-weight:500;color:var(--blue);line-height:25px}
.service-card p{position:absolute;left:8px;right:8px;font-size:15px;line-height:25.5px;color:#333}
.service-card .more{position:absolute;left:0;right:0;top:207px;font-size:14.5px;color:var(--blue);font-weight:500}
.icon-box{position:absolute;width:107px;height:108px;background:var(--blue);display:flex;align-items:center;justify-content:center}
.sq-g{position:absolute;width:24px;height:24px;background:var(--green)}
.sq-o{position:absolute;width:32px;height:31px;background:var(--orange)}
/* blog */
.blog-card{position:absolute;top:2136px;width:308px;height:401px;background:var(--white);box-shadow:0 4px 10px rgba(0,0,0,.12)}
.blog-img{width:308px;height:224px}
.blog-date{position:absolute;left:15px;top:260px;font-size:14px;color:#444}
.blog-card h4{position:absolute;left:15px;top:288px;font-size:18px;font-weight:500;color:var(--ink)}
.blog-card .btn{position:absolute;left:15px;top:338px;width:97px;height:32px;line-height:32px;font-size:12.5px}
/* contact */
.contact{left:0;top:2585px;width:1200px;height:700px;background:var(--grey-light)}
.contact-strip{left:6px;top:2585px;width:1158px;height:56px;background:var(--white)}
.field{position:absolute;background:var(--white);font-size:17px;color:#777;padding-left:28px}
.submit{left:521px;top:3041px;width:179px;height:61px;line-height:61px;font-size:18px}
.info-icon{position:absolute;top:3168px;width:56px;height:56px;display:flex;align-items:center;justify-content:center}
.info-text{position:absolute;font-size:15.5px;line-height:19px;color:#333}
/* footer */
.footer-shape{left:0;top:3220px;width:1200px;height:371px}
.site-footer .brand{position:absolute;left:84px;top:3378px;color:var(--white);font-size:30px}
.site-footer .brand-mark{background:var(--white);width:20px;height:20px}
.foot-nav{position:absolute;top:3405px;left:0;width:1200px;font-size:18px;color:var(--white)}
.foot-nav span{position:absolute}
.foot-sep{position:absolute;top:3403px;width:2px;height:28px;background:var(--white)}
.foot-rule{left:85px;top:3484px;width:1031px;height:1px;background:rgba(255,255,255,.4)}
.copyright{left:86px;top:3519px;font-size:12.5px;color:var(--white)}
.social{position:absolute;top:3514px;width:26px;height:26px;border:1.5px solid var(--white);border-radius:50%}
</style>
</head>
<body>

<header class="site-header abs">
  <div class="brand"><span class="brand-mark"></span>Quorvex<br>Labworks</div>
  <nav class="main-nav">
    <a style="left:662px">Home</a>
    <a style="left:746px">Services<span class="caret">▼</span></a>
    <a style="left:850px">Products</a>
    <a style="left:956px">Blog</a>
    <a style="left:1026px">Contact Us</a>
  </nav>
</header>

<section class="hero abs" role="img" aria-label="Team of consultants working together at a desk with a computer">
  <div class="hero-content">
    <h1>ADVANCING INNOVATION<br>THROUGH IT CONSULTING</h1>
    <p>Empower your digital journey with our advanced IT solutions.<br>From data to web and mobile apps, we've got you covered</p>
    <a class="btn">Know More</a>
    <div class="dots"><i></i><i></i><i></i><i></i></div>
  </div>
</section>

<h2 class="section-title about-title">About Quorvex Labworks</h2>
<p class="section-title about-sub">Advancing Innovation Through IT Consulting</p>
<div class="about-photo abs" role="img" aria-label="Consultants discussing data on tablets at a meeting table"></div>
<p class="about-text abs">We are a forward-thinking IT consulting firm specializing in providing cutting-edge data analytics, web application development, and mobile app development services.<br>Our passion for innovation and technology drives us to deliver tailor-made solutions</p>
<a class="btn about-btn abs">Read More</a>

<section class="services abs"></section>
<h2 class="section-title wide-title" style="top:1252px">OUR SERVICES</h2>

<div class="service-card" style="left:84px">
  <h3 style="top:82px">Data Analytics</h3>
  <p style="top:116px">Lorem ipsum dolor sit amet,<br>consec tetur adipiscing elit<br>Lorem ipsum dolor sit amet</p>
  <span class="more">Read More...</span>
</div>
<div class="service-card" style="left:347px">
  <h3>Web Development</h3>
  <p style="top:116px">Lorem ipsum dolor sit amet,<br>consec tetur adipiscing elit<br>Lorem ipsum dolor sit amet</p>
  <span class="more">Read More...</span>
</div>
<div class="service-card" style="left:610px">
  <h3>Mobile App<br>Development</h3>
  <p style="top:141px">Lorem ipsum dolor sit amet,<br>consec tetur adipiscing elit</p>
  <span class="more">Read More...</span>
</div>
<div class="service-card" style="left:872px">
  <h3>Start-up Partner</h3>
  <p style="top:116px">Lorem ipsum dolor sit amet,<br>consec tetur adipiscing elit<br>Lorem ipsum dolor sit amet</p>
  <span class="more">Read More...</span>
</div>

<!-- service icons -->
<div class="sq-g" style="left:245px;top:1387px"></div><div class="sq-o" style="left:269px;top:1411px"></div>
<div class="icon-box" style="left:152px;top:1424px">
  <svg width="70" height="56" viewBox="0 0 70 56" fill="none" stroke="#fff" stroke-width="3"><path d="M4 4v46h40"/><path d="M14 44V22M22 44V12M30 44V26"/><circle cx="44" cy="30" r="11"/><path d="M52 38l12 12"/></svg>
</div>
<div class="sq-g" style="left:508px;top:1387px"></div><div class="sq-o" style="left:532px;top:1411px"></div>
<div class="icon-box" style="left:415px;top:1424px">
  <svg width="70" height="56" viewBox="0 0 70 56" fill="#fff"><circle cx="14" cy="12" r="8"/><path d="M2 52c0-16 6-24 12-24s10 4 12 10h-6v14z"/><rect x="26" y="14" width="40" height="28" rx="2" fill="none" stroke="#fff" stroke-width="3"/><rect x="22" y="42" width="48" height="4"/><circle cx="44" cy="28" r="4"/><circle cx="54" cy="22" r="3"/></svg>
</div>
<div class="sq-g" style="left:772px;top:1387px"></div><div class="sq-o" style="left:796px;top:1411px"></div>
<div class="icon-box" style="left:679px;top:1424px">
  <svg width="40" height="56" viewBox="0 0 40 56" fill="none" stroke="#fff" stroke-width="3"><rect x="6" y="4" width="28" height="48" rx="4"/><path d="M16 10h8"/><circle cx="20" cy="45" r="2" fill="#fff"/><circle cx="18" cy="27" r="4"/><circle cx="25" cy="22" r="2.5"/></svg>
</div>
<div class="sq-g" style="left:1034px;top:1387px"></div><div class="sq-o" style="left:1058px;top:1411px"></div>
<div class="icon-box" style="left:941px;top:1424px">
  <svg width="48" height="60" viewBox="0 0 48 60" fill="#fff"><path d="M24 2c9 8 12 18 12 30l-4 8H16l-4-8C12 20 15 10 24 2z"/><circle cx="24" cy="24" r="5" fill="#2f6db5"/><path d="M12 32l-8 12 10-2zM36 32l8 12-10-2z"/><path d="M20 44h8l-4 12z"/></svg>
</div>

<h2 class="section-title wide-title" style="top:2000px">LATEST BLOG</h2>

<article class="blog-card" style="left:85px">
  <div class="blog-img" role="img" aria-label="Business meeting around a conference table" style="background:linear-gradient(135deg,#d9dbd8,#8a8c86 55%,#c9c5bb)"></div>
  <span class="blog-date">2 APRIL 2023</span>
  <h4>Lorem ipsum dolor sit amet</h4>
  <a class="btn">Read More</a>
</article>
<article class="blog-card" style="left:443px">
  <div class="blog-img" role="img" aria-label="Team gathered around a laptop" style="background:linear-gradient(135deg,#3a3c40,#9a8f86 50%,#dcd6cf)"></div>
  <span class="blog-date">20 APRIL 2023</span>
  <h4>Sit ametconsect etuadip...</h4>
  <a class="btn">Read More</a>
</article>
<article class="blog-card" style="left:803px">
  <div class="blog-img" role="img" aria-label="Top view of colleagues joining hands over a wooden table" style="background:linear-gradient(135deg,#b4a89a,#7a5440 45%,#8d6248 70%,#c7bcb0)"></div>
  <span class="blog-date">22 APRIL 2023</span>
  <h4>Lorem ipsum dolor sit amet</h4>
  <a class="btn">Read More</a>
</article>

<section class="contact abs"></section>
<div class="contact-strip abs"></div>
<h2 class="section-title wide-title" style="top:2716px">CONTACT US</h2>

<div class="field" style="left:85px;top:2833px;width:413px;height:74px;line-height:74px">First Name*</div>
<div class="field" style="left:514px;top:2833px;width:293px;height:74px;line-height:74px">Phone Number*</div>
<div class="field" style="left:824px;top:2833px;width:292px;height:74px;line-height:74px">Email Address*</div>
<div class="field" style="left:85px;top:2928px;width:1031px;height:94px;padding-left:21px;padding-top:22px">Message*</div>
<a class="btn submit abs">Submit</a>

<div class="info-icon" style="left:85px;background:var(--blue)">
  <svg width="22" height="30" viewBox="0 0 22 30"><path d="M11 0C5 0 0 5 0 11c0 8 11 19 11 19s11-11 11-19C22 5 17 0 11 0z" fill="#fff"/><circle cx="11" cy="11" r="4" fill="#2f6db5"/></svg>
</div>
<p class="info-text" style="left:160px;top:3178px">Suite 12/40 Harbourline Road,<br>Eastvale WA 6190</p>
<div class="info-icon" style="left:427px;background:var(--orange)">
  <svg width="28" height="28" viewBox="0 0 24 24"><path d="M6.6 10.8a15 15 0 006.6 6.6l2.2-2.2c.3-.3.7-.4 1-.2 1.1.4 2.3.6 3.6.6.6 0 1 .4 1 1V20c0 .6-.4 1-1 1A17 17 0 013 4c0-.6.4-1 1-1h3.5c.6 0 1 .4 1 1 0 1.3.2 2.5.6 3.6.1.3 0 .7-.2 1z" fill="#fff"/></svg>
</div>
<p class="info-text" style="left:492px;top:3186px">+61 (08) 5550 2741 (Sales / Support)</p>
<div class="info-icon" style="left:801px;background:var(--green)">
  <svg width="32" height="22" viewBox="0 0 32 22" fill="none" stroke="#fff" stroke-width="2"><rect x="1" y="1" width="30" height="20"/><path d="M1 1l15 11L31 1M1 21l11-10M31 21L20 11"/></svg>
</div>
<p class="info-text" style="left:868px;top:3186px">hello@quorvexlab.example</p>

<footer class="site-footer">
  <svg class="footer-shape abs" viewBox="0 0 1200 371" width="1200" height="371">
    <polygon points="0,27 864,132 0,50" fill="#5cb83f"/>
    <polygon points="864,132 1200,6 1200,28" fill="#f7941d"/>
    <polygon points="0,48 864,132 1200,26 1200,371 0,371" fill="#2f6db5"/>
  </svg>
  <div class="brand"><span class="brand-mark"></span>Quorvex<br>Labworks</div>
  <div class="foot-nav">
    <span style="left:605px">Home</span>
    <span style="left:698px">Services</span>
    <span style="left:818px">Products</span>
    <span style="left:935px">Blog</span>
    <span style="left:1013px">Contact us</span>
  </div>
  <i class="foot-sep" style="left:677px"></i>
  <i class="foot-sep" style="left:790px"></i>
  <i class="foot-sep" style="left:913px"></i>
  <i class="foot-sep" style="left:993px"></i>
  <div class="foot-rule abs"></div>
  <p class="copyright abs">Copyright @&nbsp; 2023 All rights reserved</p>
  <i class="social" style="left:946px"></i>
  <i class="social" style="left:990px"></i>
  <i class="social" style="left:1037px"></i>
  <i class="social" style="left:1085px"></i>
</footer>

</body>
</html>
```